Maple Bug Guard Business Cards

A modern business card with a predominantly white background and a sleek design featuring Maple with complimentary greys or blacks to convey a professional and contemporary look.

Front:
Primarily white background. Limited use of company purple color can be neighbored by greys.
Text: Name, Title, Cell Phone, Office Phone, Website, email address

Back:
Background Continuation: The back of the card maintains the white background for consistency.
Company name “Maple” in company color and font, “Bug Guard” underneath or underneath left justified of “Maple.”
A subtle pattern or texture in shades of grey to add depth behind the company Logo in font.

logo color: hex #6212ab
font: antique olive nord D Regular

```html
<!DOCTYPE html>
<html lang="en">
<head>
<meta charset="utf-8">
<title>Maple Bug Guard Business Cards</title>
<link rel="stylesheet" href="https://fonts.googleapis.com/css2?family=Montserrat:wght@400;500;700;800&display=swap">
<style>
  :root {
    --brand: #6212ab;
    --ink: #2b2b2b;
    --grey: #555555;
    --paper: #ffffff;
    --backdrop: #3a3a3c;
  }
  * { margin: 0; padding: 0; box-sizing: border-box; }
  html, body {
    width: 1200px; height: 1200px; overflow: hidden;
    background: var(--backdrop);
    font-family: "Montserrat", sans-serif;
  }
  .sheet {
    position: relative; width: 1200px; height: 1200px;
    display: flex; flex-direction: column; align-items: center; justify-content: center; gap: 70px;
  }
  .card {
    position: relative; width: 840px; height: 480px;
    background: var(--paper);
    border-radius: 40px;
    border-bottom: 5px solid var(--brand);
    overflow: hidden;
  }
  .accent-band {
    position: absolute; bottom: 52px; height: 20px;
    left: 48%; width: 38%;
    background: var(--brand);
  }
  .accent-band::before {
    content: ""; position: absolute; left: -6%; bottom: -10px; width: 12%; height: 20px;
    background: var(--brand);
  }
  .wordmark {
    position: absolute; color: var(--brand); font-weight: 800; line-height: 0.9;
  }
  .wordmark .name-main { display: block; letter-spacing: -0.02em; }
  .wordmark .name-sub { display: block; letter-spacing: 0.32em; text-transform: uppercase; }

  .card-front .wordmark { right: 90px; top: 120px; }
  .card-front .name-main { font-size: 96px; }
  .card-front .name-sub { font-size: 22px; margin-top: 8px; }

  .card-back .wordmark { left: 50%; top: 46%; transform: translate(-50%, -50%); }
  .card-back .name-main { font-size: 170px; }
  .card-back .name-sub { font-size: 36px; margin-top: 14px; }

  .contact { position: absolute; left: 70px; bottom: 110px; }
  .person-name { color: var(--brand); font-weight: 700; font-size: 38px; letter-spacing: -0.01em; }
  .person-title { color: var(--grey); font-weight: 500; font-size: 22px; margin-bottom: 18px; }
  .contact-list { list-style: none; }
  .contact-list li {
    display: flex; align-items: center; gap: 12px;
    color: var(--ink); font-size: 22px; line-height: 1.45;
  }
  .contact-list svg { width: 22px; height: 22px; flex: none; fill: var(--brand); }
</style>
</head>
<body>
<main class="sheet">
  <section class="card card-front" aria-label="Card front">
    <div class="wordmark">
      <span class="name-main">Maple</span>
      <span class="name-sub">Bug Guard</span>
    </div>
    <div class="contact">
      <p class="person-name">FULL NAME</p>
      <p class="person-title">TITLE</p>
      <ul class="contact-list">
        <li><svg viewBox="0 0 24 24" aria-hidden="true"><path d="M7 2h10a2 2 0 0 1 2 2v16a2 2 0 0 1-2 2H7a2 2 0 0 1-2-2V4a2 2 0 0 1 2-2zm0 3v13h10V5zm5 14.2a1 1 0 1 0 0 .1z"/></svg>555-014-2283</li>
        <li><svg viewBox="0 0 24 24" aria-hidden="true"><path d="M6.6 10.8a15 15 0 0 0 6.6 6.6l2.2-2.2a1 1 0 0 1 1-.25 11.4 11.4 0 0 0 3.6.57 1 1 0 0 1 1 1V20a1 1 0 0 1-1 1A17 17 0 0 1 3 4a1 1 0 0 1 1-1h3.5a1 1 0 0 1 1 1c0 1.25.2 2.45.57 3.57a1 1 0 0 1-.25 1z"/></svg>555-014-2284</li>
        <li><svg viewBox="0 0 24 24" aria-hidden="true"><path d="M12 2a10 10 0 1 0 0 20 10 10 0 0 0 0-20zm6.9 6h-3a15.6 15.6 0 0 0-1.4-3.6A8 8 0 0 1 18.9 8zM12 4a14 14 0 0 1 1.9 4h-3.8A14 14 0 0 1 12 4zM4.3 14a8 8 0 0 1 0-4h3.4a16.5 16.5 0 0 0 0 4zm.8 2h3a15.6 15.6 0 0 0 1.4 3.6A8 8 0 0 1 5.1 16zm3-8h-3a8 8 0 0 1 4.4-3.6A15.6 15.6 0 0 0 8.1 8zM12 20a14 14 0 0 1-1.9-4h3.8A14 14 0 0 1 12 20zm2.3-6H9.7a14.7 14.7 0 0 1 0-4h4.6a14.7 14.7 0 0 1 0 4zm.2 5.6a15.6 15.6 0 0 0 1.4-3.6h3a8 8 0 0 1-4.4 3.6zm1.8-5.6a16.5 16.5 0 0 0 0-4h3.4a8 8 0 0 1 0 4z"/></svg>www.maplebugguard.com</li>
        <li><svg viewBox="0 0 24 24" aria-hidden="true"><path d="M2 5h20v14H2zm2 2v.5l8 5.5 8-5.5V7zm0 2.9V17h16V9.9l-8 5.5z"/></svg>service@maplebugguard.com</li>
      </ul>
    </div>
    <div class="accent-band"></div>
  </section>

  <section class="card card-back" aria-label="Card back">
    <div class="wordmark">
      <span class="name-main">Maple</span>
      <span class="name-sub">Bug Guard</span>
    </div>
    <div class="accent-band"></div>
  </section>
</main>
</body>
</html>
```